Friendly, Professional, Simple Catering Menu

Currently we cater but don't have a take-out menu for customers to order from or see our options and we want to change that. Most of the customers we cater are employees of large and small businesses, we also have some private parties we cater to as well. With this in mind we are looking for a professional looking menu but also to have some personal touch with it. The format should be easy to read and understand. We are looking to hand out this menu to local businesses, schools and offices, and maybe after a few trial runs, our store too. Locally, we have a pretty established name but our options can't be seen by the public and we are looking to make that possible with this catering menu. Originally we were thinking of tri-fold menu, 8.5inx14in, but after seeing some of the work done already we trust the designers to create something they think would be the right fit. We don't want it too large nor too small to ensure it won't be an inconvenience for businesses, it must still stand out enough to grab their attention.
Target Market(s)
Businesses, Schools, Office buildings, and Private parties.
Industry/Entity Type
Catering

```html
<!DOCTYPE html>
<html lang="en">
<head>
<meta charset="utf-8">
<title>Ladle &amp; Loaf Catering Menu</title>
<link href="https://fonts.googleapis.com/css2?family=EB+Garamond:wght@400;500;700&display=swap" rel="stylesheet">
<style>
:root{
  --ink:#1f1b18;
  --red:#b3272b;
  --cream:#f6eed9;
  --frame:#eadfc3;
  --gold:#e9b52a;
  --paper:#ffffff;
  --tomato:#d9662f;
  --greens:#8dbb4a;
  --chili:#8c2a1c;
  --crock:#b8262b;
  --bread:#d8b07a;
}
*{margin:0;padding:0;box-sizing:border-box}
html,body{width:1200px;height:729px;overflow:hidden;background:var(--paper)}
body{font-family:"EB Garamond",Georgia,serif;color:var(--ink);position:relative}
.menu{position:relative;width:1200px;height:729px;overflow:hidden}
.photo{position:absolute;border-radius:50%;border:4px solid var(--frame)}
.frame{position:absolute;border:2px solid var(--frame);border-top:none}
.ribbon{position:absolute}
.ribbon svg{position:absolute;inset:0;width:100%;height:100%}
.ribbon h2{position:relative;font-weight:400;color:var(--red);text-align:center;text-transform:uppercase;letter-spacing:.3px;font-size:20px;line-height:1}
.column{position:absolute;text-align:center}
.item-name{font-size:18px;font-weight:400;line-height:1.15;margin-top:3px}
.item-body{font-size:13.2px;line-height:17.2px}
.intro-box{position:absolute;left:422px;top:43px;width:355px;height:161px;border:2px solid var(--gold);background:var(--paper);text-align:center;padding:8px 10px 0}
.intro-box h3{font-size:13px;font-weight:700;line-height:17px}
.intro-box p{font-size:12.8px;line-height:17.2px}
.bar-list{font-size:12.8px;line-height:17.1px}
.bar-list b{font-weight:700}
.sub-head{font-size:17.5px;font-weight:400;line-height:1.2;margin:4px 0 1px}
.prices{font-size:12.8px;line-height:17.2px}
.prices b{font-weight:700}
</style>
</head>
<body>
<div class="menu">

  <!-- frames -->
  <div class="frame" style="left:88px;top:100px;width:312px;height:700px;border-left:none"></div>
  <div class="frame" style="left:400px;top:100px;width:378px;height:700px;border-left:none"></div>
  <div class="frame" style="left:804px;top:70px;width:352px;height:540px;border-bottom:2px solid var(--frame)"></div>

  <!-- photo areas -->
  <div class="photo" role="img" aria-label="Bowl of creamy tomato basil soup" style="left:-40px;top:-45px;width:170px;height:170px;background:radial-gradient(circle,var(--tomato) 45%,#f2efe9 48%)"></div>
  <div class="photo" role="img" aria-label="Bowl of chili topped with cheddar" style="left:262px;top:-75px;width:210px;height:170px;background:radial-gradient(circle at 45% 55%,var(--chili) 35%,#f5f2ec 38%)"></div>
  <div class="photo" role="img" aria-label="Garden salad with cherry tomatoes and cucumbers" style="left:-50px;top:132px;width:158px;height:158px;background:radial-gradient(circle,var(--greens),#5d8f2e)"></div>
  <div class="photo" role="img" aria-label="Chef salad with eggs, cheese and tomatoes" style="left:-50px;top:308px;width:158px;height:168px;background:radial-gradient(circle,#e8e4d2,#9fc16a)"></div>
  <div class="photo" role="img" aria-label="Salad bar tongs and toppings" style="left:-50px;top:488px;width:175px;height:175px;background:radial-gradient(circle,#6b4a2c,#2f2a24)"></div>
  <div class="photo" role="img" aria-label="Platter of croutons, meats and shredded cheese" style="left:48px;top:604px;width:205px;height:205px;background:radial-gradient(circle,#e9c46a,#6a4a2a)"></div>
  <div class="photo" role="img" aria-label="Soup in a red crock with breadsticks and side salad" style="left:253px;top:604px;width:200px;height:200px;background:radial-gradient(circle at 40% 40%,var(--crock),var(--greens))"></div>
  <div class="photo" role="img" aria-label="Creamy soup in a red mug with spoon" style="left:740px;top:630px;width:185px;height:185px;background:radial-gradient(circle,#f1e7d6 30%,var(--crock) 35%,#3a2a22)"></div>
  <div class="photo" role="img" aria-label="Chicken noodle soup in a red bowl" style="left:1070px;top:604px;width:165px;height:165px;background:radial-gradient(circle,#e7c983 35%,var(--crock) 40%)"></div>

  <!-- left: salads -->
  <div class="ribbon" style="left:90px;top:84px;width:262px;height:37px">
    <svg viewBox="0 0 262 37" preserveAspectRatio="none" aria-hidden="true"><polygon points="0,1 262,1 244,18.5 262,36 0,36 18,18.5" fill="var(--cream)" stroke="var(--red)" stroke-width="1.5"/></svg>
    <h2 style="padding-top:10px">Salads</h2>
  </div>
  <div class="column" style="left:98px;top:124px;width:250px">
    <h3 class="item-name">Garden Salad</h3>
    <p class="item-body">Cucumbers, tomatoes, cheddar cheese, and iceberg lettuce.<br>Small: $15.00 (serves 6-12)<br>Medium: $30.00 (serves 13-24)<br>Large: $45.00 (serves 25-35)</p>
    <h3 class="item-name">Caesar Salad</h3>
    <p class="item-body">Croutons, chicken, bacon, parmesan cheese, and romaine lettuce.<br>Small: $20.00 (serves 6-12)<br>Medium: $35.00 (serves 13-24)<br>Large: $50.00 (serves 25-35)</p>
    <h3 class="item-name">Chef Salad</h3>
    <p class="item-body">Feta cheese, blue cheese, bacon,<br>chicken, chopped eggs, tomatoes,<br>iceberg and romaine lettuces.<br>Small: $20.00 (serves 6-12)<br>Medium: $35.00 (serves 13-24)<br>Large: $50.00 (serves 25-35)</p>
    <h3 class="item-name">Design Your Own Salad</h3>
    <p class="item-body">Pick one lettuce, one meat, one cheese, up to five toppings, and 2 dressings<br>Small: $25.00 (serves 6-12)<br>Medium: $40.00(serves 13-24)<br>Large: $55.00 (serves 25-35)</p>
  </div>

  <!-- middle -->
  <div class="intro-box">
    <h3>Our Famous Five Soups</h3>
    <p>5 soups we have everyday in our restaurants and we also include 2 Traveler Soups, in total we have about 50 Traveler Soups that are on a staggered 2-day rotation, meaning if today we have one “new” Traveler Soup and one “old” Traveler Soup, tomorrow the “new” Traveler Soup will become the “old” Traveler Soup and another “new” Traveler Soup will take it’s place.</p>
  </div>
  <div class="ribbon" style="left:406px;top:216px;width:382px;height:35px">
    <svg viewBox="0 0 382 35" preserveAspectRatio="none" aria-hidden="true"><polygon points="0,1 382,1 364,17.5 382,34 0,34 18,17.5" fill="var(--cream)" stroke="var(--red)" stroke-width="1.5"/></svg>
    <h2 style="padding-top:8px">The Ladle &amp; Loaf Salad Bar</h2>
  </div>
  <div class="column" style="left:420px;top:256px;width:345px">
    <p class="bar-list">Our portable salad bar fits 12 items, a bowl of lettuce, and 3 dressings.&nbsp; Choose any 12 products from our extensive list of options for your salad bar.</p>
    <h3 class="sub-head">Ladle &amp; Loaf produce!</h3>
    <p class="bar-list"><b>Lettuces —</b> Romaine, Spinach, Iceberg.<br><b>Meats</b> — Chicken, Pepperoni, Bacon, Ham.<br><b>Cheeses —</b> Shredded Parmesan Cheese, Feta Cheese, Blue Cheese, Cheddar Cheese.<br><b>Toppings —</b> Tomato’s, Olives, Beets, Mushrooms, Peas, Carrots, Onions, Green-Bell Peppers, Cabbage, Brussels Sprouts, Cauliflower, Baby Corn, Cucumbers, Broccoli, Celery, Radishes, Pickles, Pears, Pineapple, Peaches, Oranges, Mixed Fruit, Black Beans, Garbonzo Beans, Kidney Beans, Artichoke, Sweet Pickle, Pepperoncini’s, Halved Pickles, Chow Mein, Croutons, Cranberries, Walnuts, Seeds, Tortilla Strips, Cottage Cheese.<br><b>Dressings —</b> Ranch, Fat Free Ranch, Caesar, Blue Cheese, Raspberry Vinaigrette, Balsamic Vinaigrette, French dressing, Thousand Island, Spicy Southwest Ranch, Italian, Honey Mustard, Salsa,<br>Olive Oil, Vinegar.</p>
    <p class="bar-list" style="margin-top:6px">$150 — Extra lettuce, meats, cheeses, toppings and dressings available for an additional cost.</p>
  </div>

  <!-- right -->
  <div class="ribbon" style="left:786px;top:45px;width:388px;height:37px">
    <svg viewBox="0 0 388 37" preserveAspectRatio="none" aria-hidden="true"><polygon points="0,1 388,1 370,18.5 388,36 0,36 18,18.5" fill="var(--cream)" stroke="var(--red)" stroke-width="1.5"/></svg>
    <h2 style="padding-top:9px">Ladle &amp; Loaf’s Famous Five</h2>
  </div>
  <div class="column" style="left:815px;top:86px;width:330px">
    <p class="bar-list">Baked Potato with Bacon, Chicken Noodle, Clam Chowder, Creamy Tomato Basil, and Chili</p>
    <h3 class="sub-head">Travelers List:</h3>
    <p class="bar-list">Amazing Corn Chowder, Albondigas (Meatball) Soup, Beef Steak and Noodle, Bistro Spinach Artichoke, Cheeseburger Soup, Cheesy Chicken Noodle, Cheesy Potato with Bacon, Chicken Dumpling Soup, Chicken Enchilada, Chicken Fajita, Chicken Gumbo, Chicken with Wild Rice and Mushroom Soup, Chipotle Chicken Chowder, Classic Cream of Mushroom, Cowboy Campfire Soup, Cream of Asparagus, Cream of Asparagus with Cheese, Cream of Broccoli with Cheese, Fiesta Tortilla Chicken Soup, French Onion Soup, Grandma’s Chicken and Rice Soup, Great Northern Bean and Ham Soup, Hearty Grains and Beef, Italian Wedding Soup, Kickin’ Chicken Noodle, Kickin’ Pepper Jack Broccoli and Potato Soup, Kickin’ Pepper Jack Cheeseburger Soup, Nora’s Lasagna Soup, Manhattan Clam Chowder, Edie’s Mushroom Soup, Mediterranean Veggie Chicken Noodle Soup, Mediterranean Veggie Soup, Mediterranean Veggie Noodle Soup, Normandy Veggie with Cheese Soup, Pumpkin Bisque, Red Beans and Rice Soup, Roasted Red Pepper Bisque, Roasted Red Pepper Bisque with Cheese Tortellini, Royal Bean and Bacon Soup, Stuffed Bell Pepper Soup, Swiss Mushroom Cheeseburger Soup, Tomato Basil with Cheese Tortellini, White Chicken Chili, Wisconsin Cheddar, and Zesty Taco Soup.</p>
    <p class="prices" style="margin-top:8px">Small — $35 (serves 12-16)<br>Medium — $45 (serves 17-25)<br>-Large — $70 (serves 26-34)<br><b>Soup to go!</b><br>½ Gallon — $17.49<br>1 Gallon — $34.99</p>
  </div>

</div>
</body>
</html>
```